Professional BBQ Cleaning Flyer (Before & After Focus)

We need a clean, professional double-sided A5 flyer for a BBQ cleaning business.
This flyer will be handed directly to:
Property managers
Retirement villages
Over 50s communities
Resorts / body corporate
The design must feel professional, trustworthy, and easy to read β not cluttered or cheap.
π― Goal
Use a strong before & after BBQ image to show the value of the service, and position the business as reliable for communal BBQ cleaning.
π Size & Format
A5 (148 x 210mm)
Portrait (vertical)
Double-sided
Print-ready (with bleed)
π¨ Style & Branding
Colours: Red, Black, White
Clean, modern, minimal
Strong, easy-to-read fonts (important for older audience)
Plenty of white space
No emojis, no clutter, no cheap design elements
π₯ FRONT SIDE (IMPORTANT β MAIN FOCUS)
Must include:
Headline:
Professional BBQ Cleaning
For Shared & Communal Areas
Subheadline:
Keep your BBQs clean, safe, and ready for residents & guests
Main Visual :
Side-by-side BEFORE & AFTER BBQ
This is the main focus of the flyer
Must be realistic and high quality
Labels under images:
BEFORE β Greasy β’ Dirty β’ Unsafe
AFTER β Clean β’ Hygienic β’ Ready to Use
Short Bullet Points:
Deep clean of grills, burners & internal components
Ideal for retirement villages, resorts & body corporate
Multiple BBQs cleaned in one visit
Trust Line:
Fully insured & police checked
Call to Action (bottom):
Get a Quote or Book a Service
0428 593 214
www.grillshinecrew.example.au
β¬ BACK SIDE (CREDIBILITY & DETAIL)
Headline:
Trusted by Property Managers & Facilities Teams
Whatβs Included:
Full dismantle and deep clean
Removal of grease, carbon & built-up residue
Grills, burners, trays & surfaces cleaned
Reassembled and checked
Why Choose Us:
Professional, reliable service
Works around your schedule
Ideal for high-use communal BBQ areas
One-off or ongoing maintenance
Ideal For:
Retirement villages
Apartment complexes
Resorts
Body corporate properties
Closing Line:
Keep your shared BBQ areas clean, safe, and presentable year-round
Contact:
Grill Shine Crew
0428 593 214
www.grillshinecrew.example.au
grillshinecrew@mailbox.example

```html
<!DOCTYPE html>
<html lang="en">
<head>
<meta charset="UTF-8">
<title>Grill Shine Crew – Trusted by Property Managers</title>
<link href="https://fonts.googleapis.com/css2?family=Jost:wght@400;500;600&family=League+Spartan:wght@800&display=swap" rel="stylesheet">
<style>
  :root {
    --red: #db253b;
    --black: #111111;
    --ink: #2b2b2b;
    --white: #ffffff;
    --steel-dark: #5a5d62;
    --steel-light: #c8ccd1;
    --shirt: #8fb2de;
    --apron: #2c3f75;
  }
  * { margin: 0; padding: 0; box-sizing: border-box; }
  html, body { width: 846px; height: 1200px; overflow: hidden; background: var(--white); }
  .flyer {
    position: relative; width: 846px; height: 1200px; overflow: hidden;
    font-family: "Jost", "Futura", sans-serif; color: var(--ink); background: var(--white);
  }
  .header {
    position: absolute; left: 0; top: 0; width: 846px; height: 138px;
    background: var(--red); padding: 21px 0 0 20px;
  }
  .header h1 {
    font-family: "League Spartan", "Jost", sans-serif; font-weight: 800;
    font-size: 50px; line-height: 49px; color: var(--white); letter-spacing: 0.4px;
    text-transform: uppercase; white-space: nowrap;
  }
  .header h1 .lead { color: var(--black); }
  .section { position: absolute; }
  .section h2 { font-weight: 600; font-size: 28px; line-height: 34px; color: var(--ink); letter-spacing: -0.4px; }
  .section ul { list-style: none; margin-top: 6px; }
  .section li {
    position: relative; font-size: 26.5px; line-height: 40.3px; font-weight: 400;
    padding-left: 25px; color: var(--ink); white-space: nowrap;
  }
  .section li::before {
    content: ""; position: absolute; left: 3px; top: 17px;
    width: 9px; height: 9px; border-radius: 50%; background: var(--ink);
  }
  .included { left: 58px; top: 156px; }
  .why { left: 316px; top: 400px; }
  .ideal { left: 58px; top: 679px; }
  .photo {
    position: absolute; left: 0; top: 387px; width: 293px; height: 263px;
    background:
      linear-gradient(90deg, rgba(255,255,255,0) 62%, var(--white) 100%),
      linear-gradient(180deg, var(--steel-dark) 0%, #8b8f95 35%, var(--steel-light) 70%, #a7acb3 100%);
  }
  .photo::before {
    content: ""; position: absolute; left: 0; top: 0; width: 90px; height: 263px;
    background: linear-gradient(180deg, var(--shirt) 0%, var(--shirt) 40%, var(--apron) 40%, var(--apron) 100%);
  }
  .closing {
    position: absolute; left: 0; top: 903px; width: 846px; text-align: center;
    font-weight: 600; font-size: 30px; line-height: 40px; color: var(--ink); letter-spacing: -0.3px;
  }
  .closing .accent { color: var(--red); }
  .footer {
    position: absolute; left: 0; top: 1017px; width: 846px; height: 183px; background: var(--red);
  }
  .brand {
    position: absolute; left: 36px; top: 85px; display: flex; align-items: center; gap: 12px;
    color: var(--white); font-weight: 600; font-size: 25px;
  }
  .brand .dot { width: 34px; height: 34px; border-radius: 50%; background: var(--white); }
  .contact { position: absolute; right: 22px; top: 14px; text-align: right; color: var(--white); }
  .phone {
    display: flex; align-items: center; justify-content: flex-end; gap: 12px;
    font-weight: 600; font-size: 54px; line-height: 60px; letter-spacing: 1px;
  }
  .line {
    display: flex; align-items: center; justify-content: flex-end; gap: 10px;
    font-size: 29px; line-height: 42px; font-weight: 400; letter-spacing: 0.3px; white-space: nowrap;
  }
  .line:first-of-type { margin-top: 6px; }
  svg { display: block; }
</style>
</head>
<body>
<main class="flyer">
  <header class="header">
    <h1><span class="lead">Trusted by</span> Property Managers<br>&amp; Facilities Teams</h1>
  </header>

  <section class="section included">
    <h2>What’s Included</h2>
    <ul>
      <li>Full dismantle and deep clean</li>
      <li>Removal of grease, carbon &amp; built-up residue</li>
      <li>Grills, burners, trays &amp; surfaces cleaned</li>
      <li>Reassembled and checked</li>
    </ul>
  </section>

  <div class="photo" role="img" aria-label="Photo of a gloved technician wiping down a stainless steel BBQ grill"></div>

  <section class="section why">
    <h2>Why Choose Us</h2>
    <ul>
      <li>Professional, reliable service</li>
      <li>Works around your schedule</li>
      <li>Ideal for high-use communal BBQ areas</li>
      <li>One-off or ongoing maintenance</li>
      <li>Fully insured &amp; police checked</li>
    </ul>
  </section>

  <section class="section ideal">
    <h2>Ideal For</h2>
    <ul>
      <li>Retirement villages</li>
      <li>Apartment complexes</li>
      <li>Resorts</li>
      <li>Body corporate properties</li>
    </ul>
  </section>

  <p class="closing">Keep your shared <span class="accent">BBQ</span> areas clean, safe, and presentable<br>year-round</p>

  <footer class="footer">
    <div class="brand"><span class="dot"></span><span>Grill Shine Crew</span></div>
    <div class="contact">
      <div class="phone">
        <svg width="42" height="42" viewBox="0 0 24 24" aria-hidden="true"><path fill="#fff" d="M6.6 10.8c1.4 2.8 3.8 5.1 6.6 6.6l2.2-2.2c.3-.3.7-.4 1-.2 1.1.4 2.300.6 3.6.6.6 0 1 .4 1 1V20c0 .6-.4 1-1 1C10.6 21 3 13.4 3 4c0-.6.4-1 1-1h3.5c.6 0 1 .4 1 1 0 1.3.2 2.5.6 3.6.1.3 0 .7-.2 1z"/></svg>
        <span>0428 593 214</span>
      </div>
      <div class="line">
        <svg width="28" height="28" viewBox="0 0 24 24" aria-hidden="true" fill="none" stroke="#fff" stroke-width="1.8"><circle cx="12" cy="12" r="10"/><ellipse cx="12" cy="12" rx="4.5" ry="10"/><path d="M2 12h20M4 7h16M4 17h16"/></svg>
        <span>www.grillshinecrew.example.au</span>
      </div>
      <div class="line">
        <svg width="30" height="22" viewBox="0 0 30 22" aria-hidden="true" fill="none" stroke="#fff" stroke-width="2"><rect x="1" y="1" width="28" height="20"/><path d="M1 1l14 11L29 1M1 21l10-10M29 21L19 11"/></svg>
        <span>grillshinecrew@mailbox.example</span>
      </div>
    </div>
  </footer>
</main>
</body>
</html>
```